Corporate Identity Design Project

Marisol Tevendry Design is a small boutique event planning and Floral Art company, based in Northern Alberta. I require the creation of some corporate identity pieces. I want a minimalistic design.
Website www.marisoltevendry.com

Pieces should include
1. Business Card
Should include the company logo, name, email address, address, phone number. These will be professional printed.
These are three cards that I like:
http://cardlayoutgallerynook.com/wp-content/uploads/2010/02/Renata_Voskuilen_Roomworks_by_Pepperleaf_studio_Graphics.jpg
http://tidycardshowcase.com/wp-content/uploads/2011/06/Quietfold-Studio-Minimalist-Business-Cards_11.jpg
http://graphiclanternhub.com/wp-content/uploads/2012/03/16.minimalist-business-cards.jpg
I like letterpress, but I am open to other options.

2. Letterhead
will be professionally printed

3. Envelope

4. Fax Sheet
will be printed on home printer

5. Pocket Presentation
Like -http://fernwickgardenworks.com/img/design_step_proposal@2x.jpg

6. Invoice
Like - http://velmaquorlin.files.blogsite-example.com/2011/02/summit-strength-4-letterhead-combined.png?w=529

7. Proposal
Like something like this – this will not be printed, but rather emailed to clients
Like http://getfile7.brindlepost.com/getfile/files.brindlepost.com/tarnu-studio/qwRtZe8MmXp3LoKcV7B2nhdYJsaWeFUy6gT4rkPHvxiQbNcDzA9jsLE/Picture-52.png.scaled.500.jpg

8. Contract
Like http://www.brightkeelpromo.co.uk/images/tamsin-contract.jpg

9. Business Brochure – I have removed this piece from the project and will most likely post it as another project at a later date.

If you think that this is a project of interest to you, but feel that it is “too much” work for the price, please let me know how you would re-package it – I am open to suggestions.

Target Market(s)

Young women

Industry/Entity Type

Boutique

Requirements
Should not have
• I do not want it to look "frilly"

```html
<!DOCTYPE html>
<html lang="en">
<head>
<meta charset="utf-8">
<title>Marisol Tevendry Design – Stationery Set</title>
<link href="https://fonts.googleapis.com/css2?family=Ubuntu:ital,wght@0,400;0,500;0,700;1,400&display=swap" rel="stylesheet">
<style>
  :root {
    --rose: #bb7274;
    --rose-label: #c0787a;
    --charcoal: #3f3d3a;
    --ink: #2c2b29;
    --paper: #ffffff;
    --stage: #ececec;
    --window: #afafb1;
    --muted: #6b6a68;
  }
  * { margin: 0; padding: 0; box-sizing: border-box; }
  html, body { width: 1200px; height: 900px; overflow: hidden; }
  body {
    position: relative;
    background: var(--stage);
    font-family: "Ubuntu", "Segoe UI", sans-serif;
    color: var(--ink);
  }
  .piece { position: absolute; box-shadow: 0 2px 6px rgba(0,0,0,.18); }
  .label {
    position: absolute;
    font-size: 11px;
    letter-spacing: .08em;
    color: var(--rose-label);
  }

  /* wordmark: name in one weight, one colour, with a plain circle */
  .brand { position: absolute; display: flex; align-items: center; gap: 8px; }
  .brand-dot { border-radius: 50%; flex: none; }
  .brand-name {
    font-weight: 500;
    text-transform: uppercase;
    letter-spacing: .12em;
    line-height: 1.05;
  }
  .brand--dark .brand-name { color: var(--charcoal); }
  .brand--dark .brand-dot { background: var(--rose); }
  .brand--light .brand-name { color: #fff; }
  .brand--light .brand-dot { background: var(--charcoal); }

  .contact-row { position: absolute; display: flex; align-items: center; gap: 6px; white-space: nowrap; }
  .icon { width: 11px; height: 11px; flex: none; }

  /* envelope DL */
  .envelope-dl { left: 25px; top: 22px; width: 460px; height: 243px; background: var(--paper); }
  .window { position: absolute; background: var(--window); border-radius: 6px; }
  .envelope-dl .window { left: 40px; top: 113px; width: 205px; height: 85px; }
  .envelope-dl .contact-row { left: 37px; top: 222px; font-size: 8.5px; letter-spacing: .05em; color: var(--charcoal); gap: 14px; }

  /* business cards */
  .card { width: 191px; height: 111px; border-radius: 10px; overflow: hidden; }
  .card-front { left: 55px; top: 304px; background: var(--rose); }
  .card-front .card-tagline {
    position: absolute; left: 9px; top: 96px; font-size: 3.6px; letter-spacing: .12em; color: rgba(255,255,255,.85); white-space: nowrap;
  }
  .card-back { left: 280px; top: 304px; background: var(--paper); width: 193px; }
  .card-back .holder { position: absolute; left: 16px; top: 17px; font-size: 9.5px; color: var(--charcoal); }
  .card-back .holder b { font-weight: 700; }
  .card-back .role { position: absolute; left: 16px; top: 29px; font-size: 5.5px; color: var(--rose); font-style: italic; }
  .card-back .line { position: absolute; font-size: 4.2px; color: var(--muted); white-space: nowrap; display: flex; align-items: center; gap: 3px; }
  .card-back .line i { width: 5px; height: 5px; border-radius: 50%; background: var(--rose); display: inline-block; }
  .card-back .web { position: absolute; left: 16px; top: 95px; font-size: 5.5px; color: var(--rose); letter-spacing: .05em; }
  .card-back .web b { font-weight: 700; }

  /* envelope C5 */
  .envelope-c5 { left: 40px; top: 455px; width: 545px; height: 388px; background: var(--rose); }
  .envelope-c5 .window { left: 34px; top: 118px; width: 208px; height: 107px; background: #aeb0b1; border: 1px solid #555; border-radius: 10px; }
  .envelope-c5 .address { position: absolute; left: 56px; top: 350px; font-size: 8px; letter-spacing: .06em; color: #fff; }
  .envelope-c5 .contact-row { left: 48px; top: 364px; font-size: 8px; color: #fff; gap: 12px; }

  /* letterhead back */
  .letterhead-back { left: 661px; top: 230px; width: 458px; height: 652px; background: var(--rose); }
  .letterhead-back .tagline { position: absolute; left: 25px; top: 612px; font-size: 8.5px; letter-spacing: .07em; color: #fff; white-space: nowrap; }

  /* letterhead front */
  .letterhead-front { left: 715px; top: 143px; width: 461px; height: 652px; background: var(--paper); }
  .meta { position: absolute; right: 381px; text-align: right; font-size: 7px; line-height: 11.5px; }
  .meta dt { color: var(--rose); font-size: 8px; }
  .meta dd { color: var(--charcoal); margin-bottom: 7px; }
  .letter { position: absolute; left: 128px; top: 128px; width: 276px; font-size: 6.2px; color: var(--ink); }
  .letter .salute { margin-bottom: 6px; }
  .letter p.body { text-align: justify; line-height: 11.6px; margin-bottom: 8.5px; }
  .letter .closing { margin-top: 4px; }
  .signature { width: 104px; height: 26px; margin: 10px 0 6px -8px; background: linear-gradient(90deg, rgba(44,43,41,.0), rgba(44,43,41,.14), rgba(44,43,41,0)); }
  .letter .signer { line-height: 10px; }
  .letter-foot { position: absolute; left: 0; right: 0; top: 602px; text-align: center; color: var(--charcoal); }
  .letter-foot .address { font-size: 8.5px; letter-spacing: .06em; }
  .letter-foot .contact-row { position: static; justify-content: center; font-size: 8.5px; margin-top: 4px; gap: 10px; }
  .letter-foot .web { font-size: 9.5px; letter-spacing: .1em; margin-top: 2px; }
  .letter-foot .web b { font-weight: 700; }
</style>
</head>
<body>

<!-- shared icons -->
<svg width="0" height="0" style="position:absolute">
  <defs>
    <symbol id="icon-phone" viewBox="0 0 12 12">
      <circle cx="6" cy="6" r="6" fill="currentColor"/>
      <path d="M4.1 3.1l1 .9-.5.9c.4.9 1 1.5 1.9 1.9l.9-.5.9 1-.7.8c-1.9-.2-3.9-2.2-4.2-4.2z" fill="#fff"/>
    </symbol>
    <symbol id="icon-mail" viewBox="0 0 12 12">
      <circle cx="6" cy="6" r="6" fill="currentColor"/>
      <rect x="3" y="4" width="6" height="4.2" fill="#fff"/>
      <path d="M3 4l3 2.3L9 4" fill="none" stroke="currentColor" stroke-width=".7"/>
    </symbol>
  </defs>
</svg>

<!-- Envelope DL -->
<section class="piece envelope-dl" aria-label="DL envelope">
  <div class="brand brand--dark" style="left:305px;top:25px;">
    <span class="brand-dot" style="width:42px;height:42px;"></span>
    <span class="brand-name" style="font-size:11.5px;">Marisol<br>Tevendry<br>Design</span>
  </div>
  <div class="window"></div>
  <div class="contact-row">
    <span>Marisol Tevendry, Your Office, AB 12345</span>
    <span class="contact-row" style="position:static;gap:5px;"><svg class="icon" style="color:var(--rose)"><use href="#icon-phone"/></svg>780-555-0142</span>
    <span class="contact-row" style="position:static;gap:5px;"><svg class="icon" style="color:var(--rose)"><use href="#icon-mail"/></svg>hello@marisoltevendry.com</span>
  </div>
</section>
<span class="label" style="left:517px;top:26px;">Envelope DL</span>

<!-- Stand-alone brand lockup -->
<div class="brand brand--dark" style="left:1018px;top:40px;">
  <span class="brand-dot" style="width:48px;height:48px;"></span>
  <span class="brand-name" style="font-size:12.5px;">Marisol<br>Tevendry<br>Design</span>
</div>

<!-- Business cards -->
<section class="piece card card-front" aria-label="Business card front">
  <div class="brand brand--light" style="left:104px;top:66px;gap:4px;">
    <span class="brand-dot" style="width:16px;height:16px;"></span>
    <span class="brand-name" style="font-size:5.5px;">Marisol<br>Tevendry<br>Design</span>
  </div>
  <div class="card-tagline">EVENT STYLING | NORTHFIELD | ASPEN RIDGE | FLORAL</div>
</section>

<section class="piece card card-back" aria-label="Business card back">
  <div class="holder"><b>Marisol</b> Tevendry</div>
  <div class="role">Designer</div>
  <div class="line" style="left:16px;top:62px;">Marisol Tevendry, Your Office, AB 12345</div>
  <div class="line" style="left:16px;top:73px;"><i></i>780-555-0142</div>
  <div class="line" style="left:16px;top:82px;"><i></i>hello@marisoltevendry.com</div>
  <div class="line" style="left:90px;top:73px;"><i></i>social/marisoltevendry</div>
  <div class="line" style="left:90px;top:82px;"><i></i>page/marisoltevendry</div>
  <div class="web">www.<b>marisoltevendry</b>.com</div>
</section>
<span class="label" style="left:488px;top:356px;">Business Card</span>

<!-- Envelope C5 -->
<section class="piece envelope-c5" aria-label="C5 envelope">
  <div class="brand brand--light" style="left:68px;top:25px;">
    <span class="brand-dot" style="width:48px;height:48px;"></span>
    <span class="brand-name" style="font-size:12.5px;">Marisol<br>Tevendry<br>Design</span>
  </div>
  <div class="window"></div>
  <div class="address">Marisol Tevendry, Your Office, AB 12345</div>
  <div class="contact-row">
    <span class="contact-row" style="position:static;gap:5px;"><svg class="icon" style="color:var(--charcoal)"><use href="#icon-phone"/></svg>780-555-0142</span>
    <span class="contact-row" style="position:static;gap:5px;"><svg class="icon" style="color:var(--charcoal)"><use href="#icon-mail"/></svg>hello@marisoltevendry.com</span>
  </div>
</section>
<span class="label" style="left:43px;top:856px;">Envelope C5</span>

<!-- Letterhead back -->
<section class="piece letterhead-back" aria-label="Letterhead back">
  <div class="brand brand--light" style="left:322px;top:580px;">
    <span class="brand-dot" style="width:34px;height:34px;"></span>
    <span class="brand-name" style="font-size:11px;">Marisol<br>Tevendry<br>Design</span>
  </div>
  <div class="tagline">EVENT STYLING | NORTHFIELD | ASPEN RIDGE | FLORAL ART</div>
</section>
<span class="label" style="left:561px;top:871px;">Letterhead Back</span>

<!-- Letterhead front -->
<section class="piece letterhead-front" aria-label="Letterhead front">
  <div class="brand brand--dark" style="left:199px;top:22px;">
    <span class="brand-dot" style="width:36px;height:36px;"></span>
  </div>

  <dl class="meta" style="top:130px;">
    <dt>Subject</dt><dd>Lorem Ipsum</dd>
    <dt>Date</dt><dd>01/02/2012</dd>
    <dt>Receiver</dt><dd>Ada Lindqvist</dd>
  </dl>

  <article class="letter">
    <p class="salute">Dear Client,</p>
    <p class="body">Lorem ipsum dolor sit amet, consectetur adipisicing elit, sed do eiusmod tempor incididunt ut labore et dolore magna aliqua. Ut enim ad minim veniam, quis nostrud exercitation ullamco laboris nisi ut aliquip ex ea commodo consequat. Duis aute irure dolor in reprehenderit in voluptate velit esse cillum dolore eu fugiat nulla pariatur. Excepteur sint occaecat cupidatat non proident, sunt in culpa qui officia deserunt mollit anim id est laborum.</p>
    <p class="body">Lorem ipsum dolor sit amet, consectetur adipisicing elit, sed do eiusmod tempor incididunt ut labore et dolore magna aliqua. Ut enim ad minim veniam, quis nostrud exercitation ullamco laboris nisi ut aliquip ex ea commodo consequat. Duis aute irure dolor in reprehenderit in voluptate velit esse cillum dolore eu fugiat nulla pariatur. Excepteur sint occaecat cupidatat non proident, sunt in culpa qui officia deserunt mollit anim id est laborum.</p>
    <p class="body">Lorem ipsum dolor sit amet, consectetur adipisicing elit, sed do eiusmod tempor incididunt ut labore et dolore magna aliqua. Ut enim ad minim veniam, quis nostrud exercitation ullamco laboris nisi ut aliquip ex ea commodo consequat. Duis aute irure dolor in reprehenderit in voluptate velit esse cillum dolore eu fugiat nulla pariatur. Excepteur sint occaecat cupidatat non proident, sunt in culpa qui officia deserunt mollit anim id est laborum.</p>
    <p class="body">Lorem ipsum dolor sit amet, consectetur adipisicing elit, sed do eiusmod tempor incididunt ut labore et dolore magna aliqua. Ut enim ad minim veniam, quis nostrud exercitation ullamco laboris nisi ut aliquip ex ea commodo consequat. Duis aute irure dolor in reprehenderit in voluptate velit esse cillum dolore eu fugiat nulla pariatur. Excepteur sint occaecat cupidatat non proident, sunt in culpa qui officia deserunt mollit anim id est laborum.</p>
    <p class="body">Lorem ipsum dolor sit amet, consectetur adipisicing elit, sed do eiusmod tempor incididunt ut labore et dolore magna aliqua. Ut enim ad minim veniam, quis nostrud exercitation ullamco laboris nisi ut aliquip ex ea commodo consequat. Duis aute irure dolor in reprehenderit in voluptate velit esse cillum dolore eu fugiat nulla pariatur. Excepteur sint occaecat cupidatat non proident, sunt in culpa qui officia deserunt mollit anim id est laborum.</p>
    <p class="closing">Yours Sincerely,</p>
    <div class="signature" role="img" aria-label="Handwritten signature of Jonah Pell"></div>
    <p class="signer">Jonah Pell<br>Executive manager</p>
  </article>

  <footer class="letter-foot">
    <div class="address">Marisol Tevendry, Your Office, AB 12345</div>
    <div class="contact-row">
      <span class="contact-row" style="position:static;gap:5px;"><svg class="icon" style="color:var(--rose)"><use href="#icon-phone"/></svg>780-555-0142</span>
      <span class="contact-row" style="position:static;gap:5px;"><svg class="icon" style="color:var(--rose)"><use href="#icon-mail"/></svg>hello@marisoltevendry.com</span>
    </div>
    <div class="web">www.<b>marisoltevendry</b>.com</div>
  </footer>
</section>
<span class="label" style="left:611px;top:147px;">Letterhead Front</span>

</body>
</html>
```